A picture window of stained glass as seen in older churches,
Etched in it is the tree of life.
God lead ministry

Ministry

Harvest Lantern/Open Meadow. Ministries
Mavis Penhallow, Founder
P.O. Box 47528 Colorado Springs, CO 80917-5528
719-608-4172

Sans Serif

```html
<!DOCTYPE html>
<html lang="en">
<head>
<meta charset="utf-8">
<title>Harvest Lantern — Business Card</title>
<link rel="stylesheet" href="https://fonts.googleapis.com/css2?family=Lato:wght@300;400;700;900&display=swap">
<style>
  :root {
    --backdrop: #5b5b5b;
    --card-black: #050608;
    --card-charcoal: #15171b;
    --brand-blue: #1c9ad8;
    --band-blue: #1596d6;
    --band-edge: #1b5ea9;
    --text-white: #f2f4f7;
    --text-soft: #c9ced6;
    --glass-deep: #0a1f5c;
    --glass-mid: #1f5fb8;
    --glass-bright: #3ec0e6;
    --glass-teal: #2e9c8e;
  }
  * { margin: 0; padding: 0; box-sizing: border-box; }
  html, body {
    width: 1200px;
    height: 900px;
    overflow: hidden;
    background: var(--backdrop);
    font-family: "Lato", sans-serif;
  }
  .canvas {
    position: relative;
    width: 1200px;
    height: 900px;
  }
  .business-card {
    position: absolute;
    left: 100px;
    top: 164px;
    width: 1000px;
    height: 572px;
    overflow: hidden;
    background: linear-gradient(90deg, var(--card-black) 0%, var(--card-charcoal) 55%, var(--card-black) 100%);
  }
  .window-art {
    position: absolute;
    left: 52px;
    top: 0;
    width: 330px;
    height: 470px;
    border-radius: 165px 165px 0 0 / 120px 120px 0 0;
    background:
      radial-gradient(ellipse at 50% 40%, var(--glass-bright) 0%, var(--glass-mid) 35%, transparent 70%),
      linear-gradient(160deg, var(--glass-deep) 0%, var(--glass-mid) 45%, var(--glass-teal) 80%, var(--glass-deep) 100%);
    opacity: 0.95;
  }
  .ministry-name {
    position: absolute;
    left: 432px;
    top: 116px;
    color: var(--brand-blue);
    font-weight: 700;
    font-size: 42px;
    letter-spacing: 0.5px;
    text-transform: uppercase;
    line-height: 1;
    white-space: nowrap;
  }
  .ministry-tagline {
    position: absolute;
    left: 434px;
    top: 168px;
    color: var(--text-soft);
    font-weight: 400;
    font-size: 22px;
    letter-spacing: 0.8px;
    white-space: nowrap;
  }
  .person-name {
    position: absolute;
    left: 432px;
    top: 286px;
    color: var(--text-white);
    font-size: 36px;
    text-transform: uppercase;
    line-height: 1;
    white-space: nowrap;
  }
  .person-name .first { font-weight: 300; }
  .person-name .last { font-weight: 700; }
  .person-role {
    position: absolute;
    left: 434px;
    top: 338px;
    color: var(--brand-blue);
    font-weight: 700;
    font-size: 19px;
    letter-spacing: 3px;
    text-transform: uppercase;
  }
  .phone-line {
    position: absolute;
    left: 434px;
    top: 388px;
    display: flex;
    align-items: center;
    gap: 12px;
    color: var(--text-white);
    font-size: 25px;
    font-weight: 400;
  }
  .phone-line svg { width: 24px; height: 24px; }
  .band-edge {
    position: absolute;
    left: 0;
    right: 0;
    top: 470px;
    height: 9px;
    background: var(--band-edge);
  }
  .address-band {
    position: absolute;
    left: 0;
    right: 0;
    top: 479px;
    bottom: 0;
    background: var(--band-blue);
    display: flex;
    align-items: center;
    padding-left: 40px;
    gap: 18px;
    color: var(--text-white);
    font-weight: 700;
    font-size: 27px;
    letter-spacing: 2px;
    text-transform: uppercase;
    white-space: nowrap;
  }
  .address-band svg { width: 24px; height: 32px; flex: none; }
</style>
</head>
<body>
  <div class="canvas">
    <div class="business-card">
      <div class="window-art" role="img" aria-label="Arched leaded church window of coloured panes in blues and teals, crossed by dark frame bars"></div>

      <div class="ministry-name">Harvest Lantern</div>
      <div class="ministry-tagline">Open Meadow. Ministries</div>

      <div class="person-name"><span class="first">Mavis</span> <span class="last">Penhallow</span></div>
      <div class="person-role">Founder</div>

      <div class="phone-line">
        <svg viewBox="0 0 24 24" aria-hidden="true">
          <path fill="var(--brand-blue)" d="M3 8c0-2 2-4 9-4s9 2 9 4v2h-5V8.5c-1-.6-2.5-.8-4-.8s-3 .2-4 .8V10H3z"/>
          <path fill="var(--brand-blue)" d="M6 12h12l2 8H4z"/>
          <circle cx="12" cy="16" r="2" fill="var(--card-black)"/>
        </svg>
        <span>719-608-4172</span>
      </div>

      <div class="band-edge"></div>
      <div class="address-band">
        <svg viewBox="0 0 24 32" aria-hidden="true">
          <path fill="var(--text-white)" d="M12 0C5.4 0 0 5.2 0 11.7 0 20 12 32 12 32s12-12 12-20.3C24 5.2 18.6 0 12 0zm0 16.5a5 5 0 1 1 0-10 5 5 0 0 1 0 10z"/>
        </svg>
        <span>P.O. Box 47528 Colorado Springs, CO 80917-5528</span>
      </div>
    </div>
  </div>
</body>
</html>
```